wealth management firm, professional group, new model

we have a logo that works but we need a card, white background using our colors...clean look

our tag line if can be used in

The Path From Saver to Steward

```html
<!DOCTYPE html>
<html lang="en">
<head>
<meta charset="utf-8">
<title>Veran Wealth Partners – Business Card</title>
<link href="https://fonts.googleapis.com/css2?family=Montserrat:wght@400;500;700&display=swap" rel="stylesheet">
<style>
  :root {
    --navy: #0f2350;
    --navy-deep: #0b1d45;
    --navy-soft: #1d3366;
    --paper: #f3f4f6;
    --white: #ffffff;
    --stage: #8a8a8a;
  }
  * { box-sizing: border-box; margin: 0; padding: 0; }
  html, body { width: 1200px; height: 1050px; overflow: hidden; }
  body {
    background: var(--stage);
    font-family: "Montserrat", Arial, sans-serif;
    color: var(--navy);
    position: relative;
  }
  .card {
    position: absolute;
    left: 250px;
    width: 700px;
    height: 400px;
    border-radius: 4px;
    box-shadow: 0 14px 30px rgba(0,0,0,0.25);
    overflow: hidden;
  }

  /* Back side */
  .card--back { top: 90px; background: var(--navy-deep); }
  .back-name {
    position: absolute;
    top: 120px; left: 0; right: 0;
    text-align: center;
    font-weight: 400;
    font-size: 34px;
    letter-spacing: 10px;
    color: var(--navy-soft);
  }
  .tagline-rule {
    position: absolute;
    left: 0; right: 0; top: 270px;
    display: flex;
    align-items: center;
    gap: 14px;
  }
  .tagline-rule .line { flex: 1; height: 1.5px; background: var(--white); }
  .tagline {
    color: var(--white);
    font-size: 17px;
    font-weight: 500;
    letter-spacing: 1px;
    white-space: nowrap;
  }

  /* Front side */
  .card--front { top: 560px; background: var(--paper); }
  .brand {
    position: absolute;
    left: 50px; top: 140px;
    width: 270px;
    color: var(--navy);
  }
  .brand-name {
    font-weight: 400;
    font-size: 48px;
    letter-spacing: 22px;
    line-height: 1;
  }
  .brand-sub {
    margin-top: 16px;
    font-weight: 400;
    font-size: 15px;
    letter-spacing: 4.5px;
  }
  .divider {
    position: absolute;
    left: 345px; top: 70px;
    width: 2px; height: 260px;
    background: var(--navy);
  }
  .contact {
    position: absolute;
    left: 375px; top: 78px;
    line-height: 1.4;
    color: var(--navy);
  }
  .person-name { font-size: 25px; font-weight: 700; letter-spacing: 0.5px; line-height: 1.1; }
  .person-role { font-size: 17px; font-weight: 500; margin-bottom: 12px; }
  .address { font-size: 16px; margin-bottom: 12px; }
  .detail { display: flex; align-items: center; gap: 7px; font-size: 16px; }
  .detail svg { width: 14px; height: 14px; flex: none; fill: var(--navy); }
  .detail--phone span { letter-spacing: 2.5px; }
</style>
</head>
<body>

<section class="card card--back" aria-label="Card back">
  <div class="back-name">VERAN</div>
  <div class="tagline-rule">
    <span class="line"></span>
    <span class="tagline">The Path From Saver to Steward</span>
    <span class="line"></span>
  </div>
</section>

<section class="card card--front" aria-label="Card front">
  <div class="brand">
    <div class="brand-name">VERAN</div>
    <div class="brand-sub">WEALTH PARTNERS</div>
  </div>

  <div class="divider"></div>

  <div class="contact">
    <div class="person-name">DANIEL MARSH</div>
    <div class="person-role">Advisor</div>
    <div class="address">58 Harbor Lane<br>Cedar Bay, FL 32700</div>
    <div class="detail detail--phone">
      <svg viewBox="0 0 24 24" aria-hidden="true"><path d="M6.6 10.8a15.1 15.1 0 0 0 6.6 6.6l2.2-2.2a1 1 0 0 1 1-.25 11.4 11.4 0 0 0 3.6.57 1 1 0 0 1 1 1V20a1 1 0 0 1-1 1A17 17 0 0 1 3 4a1 1 0 0 1 1-1h3.5a1 1 0 0 1 1 1c0 1.25.2 2.45.57 3.57a1 1 0 0 1-.25 1z"/></svg>
      <span>555-014-2290</span>
    </div>
    <div class="detail">
      <svg viewBox="0 0 24 24" aria-hidden="true"><path d="M2 5h20v14H2zm2 2v.5l8 5 8-5V7zm0 2.9V17h16V9.9l-8 5z"/></svg>
      <span>info@veranwealth.com</span>
    </div>
    <div class="detail">
      <svg viewBox="0 0 24 24" aria-hidden="true"><path d="M12 2a10 10 0 1 0 0 20 10 10 0 0 0 0-20zm6.9 6h-2.9a15.6 15.6 0 0 0-1.4-3.6A8 8 0 0 1 18.9 8zM12 4c.8 1.2 1.5 2.5 1.9 4h-3.8c.4-1.5 1.1-2.8 1.9-4zM4.3 14a8 8 0 0 1 0-4h3.4a16.5 16.5 0 0 0 0 4zm.8 2h2.9c.3 1.3.8 2.5 1.4 3.6A8 8 0 0 1 5.1 16zM8 8H5.1a8 8 0 0 1 4.3-3.6C8.8 5.5 8.3 6.7 8 8zm4 12c-.8-1.2-1.5-2.5-1.9-4h3.8c-.4 1.5-1.1 2.8-1.9 4zm2.3-6H9.7a14.7 14.7 0 0 1 0-4h4.6a14.7 14.7 0 0 1 0 4zm.3 5.6c.6-1.1 1.1-2.3 1.4-3.6h2.9a8 8 0 0 1-4.3 3.6zM16.3 14a16.5 16.5 0 0 0 0-4h3.4a8 8 0 0 1 0 4z"/></svg>
      <span>veranwealth.com</span>
    </div>
  </div>
</section>

</body>
</html>
```